law firm website

We need a website for our law firm that is based in Kabul, Afghanistan. We provide legal and government affairs services for the international community. We would like to see designs that use the colors of our logo, designs that are elegant and simple, yet not boring or over the top. No law or law related symbols or pictures. We would like clocks that show times for Kabul, Dubai and Washington DC.
Reason: No designs that are up to the task as yet. Perhaps we should stop using picture of people, that obviously don't work with us, in the website. If you are to use pictures, please try using pictures of Afghanistan mountains, art, craft etc. Also, please make the clocks very small - they seem to be dominating the website. We do not sell clocks or watches - we are a law firm. Hope you all understand and thank you for your designs to date.
Deal All,
Industry/Entity Type
Government
Requirements
Must have
- our logo.
the following phrases/words in flash.
"international standards" "local expertise" "integrity" "clarity" "commitment" "Afghanistan"
clocks: kabul, dubai, washington dc
Should not have
- law related pictures
afghanistan flag colors

```html
<!DOCTYPE html>
<html lang="en">
<head>
<meta charset="utf-8">
<title>Paropamisus Legal Group</title>
<link rel="stylesheet" href="https://fonts.googleapis.com/css2?family=Open+Sans:wdth,wght@75,600;75,700&family=Vollkorn:wght@400;500&display=swap">
<style>
  :root {
    --ink-dark: #1c1c1e;
    --white: #ffffff;
    --sky-top: #3d3c40;
    --sky-mid: #6a5244;
    --sunset: #f07a2c;
    --sunset-glow: #f6a03a;
    --peak-blue: #3a4a6a;
    --valley-navy: #1a2740;
    --fog-teal: #3f8fa6;
    --fog-pale: #9fb6c4;
    --fog-pink: #e9a1ad;
    --serif: "Vollkorn", Georgia, serif;
    --condensed: "Open Sans", "Arial Narrow", sans-serif;
  }
  * { margin: 0; padding: 0; box-sizing: border-box; }
  html, body { width: 1200px; height: 750px; overflow: hidden; background: var(--valley-navy); }
  .page { position: relative; width: 1200px; height: 750px; overflow: hidden; color: var(--white); }

  .hero-image {
    position: absolute; inset: 0;
    background:
      radial-gradient(ellipse 40% 18% at 82% 85%, var(--fog-pink) 0%, rgba(233,161,173,0) 100%),
      radial-gradient(ellipse 60% 14% at 30% 32%, rgba(246,160,58,0.9) 0%, rgba(240,122,44,0) 100%),
      linear-gradient(180deg,
        var(--sky-top) 0%,
        var(--sky-mid) 18%,
        var(--sunset) 28%,
        var(--sunset-glow) 34%,
        var(--peak-blue) 44%,
        #c9d3e0 52%,
        var(--valley-navy) 64%,
        #1f3650 78%,
        var(--fog-teal) 88%,
        var(--fog-pale) 100%);
  }

  .site-header {
    position: absolute; top: 0; left: 0; right: 0; height: 68px;
    display: flex; align-items: center; justify-content: space-between;
    padding: 0 19px 0 17px;
  }
  .brand { display: flex; align-items: center; gap: 8px; font-family: var(--serif); font-size: 18px; color: var(--white); }
  .brand-square { width: 49px; height: 30px; background: var(--ink-dark); }
  .main-nav { display: flex; gap: 35px; font-family: var(--serif); font-size: 17.5px; }
  .main-nav a { color: var(--white); text-decoration: none; }

  .hero-copy {
    position: absolute; left: 0; right: 0; top: 250px;
    display: flex; flex-direction: column; align-items: center;
    font-family: var(--condensed); font-stretch: 75%; font-weight: 700; text-transform: uppercase;
  }
  .tagline { font-size: 23.5px; letter-spacing: 2.2px; line-height: 1; font-weight: 600; }
  .headline-line { font-size: 98px; line-height: 0.9; letter-spacing: 3px; }
  .headline-line.first { margin-top: 6px; }
  .rule { height: 4px; background: var(--white); }
  .rule.first { width: 551px; margin-top: 5px; }
  .rule.second { width: 433px; margin-top: 3px; }
  .headline-line.second { margin-top: 12px; }
  .subline { font-size: 23.5px; letter-spacing: 2px; line-height: 1; margin-top: 11px; font-weight: 600; }

  .scroll-cue {
    position: absolute; left: 0; right: 0; top: 690px;
    display: flex; flex-direction: column; align-items: center; gap: 4px;
    font-family: var(--condensed); font-stretch: 75%; font-size: 11.5px; letter-spacing: 0.3px; text-transform: uppercase;
  }
</style>
</head>
<body>
<div class="page">
  <div class="hero-image" role="img" aria-label="Snow-capped mountain range at sunset with an orange sky, misty valley and pine trees"></div>

  <header class="site-header">
    <div class="brand"><span class="brand-square"></span><span class="brand-name">Paropamisus Legal Group</span></div>
    <nav class="main-nav">
      <a href="#">The Firm</a>
      <a href="#">Insights</a>
      <a href="#">Practices</a>
      <a href="#">Professionals</a>
      <a href="#">Careers</a>
    </nav>
  </header>

  <section class="hero-copy">
    <p class="tagline">Driven by integrity, clarity, and our international commitment</p>
    <h1 class="headline-line first">From Nation</h1>
    <div class="rule first"></div>
    <h1 class="headline-line second">To Nation</h1>
    <div class="rule second"></div>
    <p class="subline">Serving the most complex of industries and government</p>
  </section>

  <div class="scroll-cue">
    <svg width="34" height="17" viewBox="0 0 34 17" aria-hidden="true">
      <polyline points="1,1 17,15 33,1" fill="none" stroke="#ffffff" stroke-width="1.5"/>
    </svg>
    <span>Scroll down</span>
  </div>
</div>
</body>
</html>
```